Trifold - Brantley Commercial Roofing

Enhance the look, change the images if needed. Create some interest please!

Target Market(s)

Commercial and Industrial Building Owners

Industry/Entity Type

Roofing

Font styles to use
Serif

Requirements
Must have
• Organized layout, call to action

```html
<!DOCTYPE html>
<html lang="en">
<head>
<meta charset="utf-8">
<title>Brantley Commercial Roofing – Trifold</title>
<link href="https://fonts.googleapis.com/css2?family=Montserrat:wght@400;600;700;800&family=Open+Sans:wght@400;600;700&display=swap" rel="stylesheet">
<style>
:root{
  --page:#e8e6e2;
  --charcoal:#2e2e2f;
  --charcoal-deep:#1e1e1f;
  --orange:#f08a1c;
  --navy:#1f2a5c;
  --white:#ffffff;
  --paper:#f6f6f6;
  --ink:#4a4a4a;
  --muted:#cfcfcf;
}
*{box-sizing:border-box;margin:0;padding:0}
html,body{width:1200px;height:2388px;overflow:hidden}
body{background:var(--page);font-family:"Open Sans",Arial,sans-serif;position:relative}
.spread{position:absolute;left:50px;width:1100px;height:850px;display:grid;grid-template-columns:repeat(3,1fr);box-shadow:0 10px 30px rgba(0,0,0,.18)}
.spread--outside{top:229px}
.spread--inside{top:1309px}
.panel{position:relative;overflow:hidden;height:850px}
.panel--light{background:var(--paper);color:var(--ink)}
.panel--dark{background:var(--charcoal);color:var(--white)}
.panel + .panel{border-left:1px solid rgba(0,0,0,.12)}
.skyline{position:absolute;left:0;right:0;bottom:0;height:70px;background:linear-gradient(180deg,#3a3a3b,var(--charcoal-deep))}
.panel--dark .skyline{background:linear-gradient(180deg,#262627,#151516)}
.photo{position:absolute;left:0;right:0;top:0}
.curve{position:absolute;left:0;width:100%;display:block}

/* flap */
.photo--founder{height:300px;background:linear-gradient(135deg,#6b4a36,#b08a6d 55%,#3a2c25)}
.founder{position:absolute;top:320px;left:34px;right:30px}
.founder__title{font-family:"Montserrat",Arial,sans-serif;font-weight:700;color:var(--orange);font-size:19px}
.founder__name{font-size:12px;color:#777;margin:4px 0 14px}
.founder p{font-size:11.5px;line-height:1.6;margin-bottom:10px}

/* back */
.mission{position:absolute;top:0;left:0;right:0;padding:26px 30px 0;text-align:center}
.mission__photo{width:110px;height:110px;border-radius:50%;margin:0 auto 14px;border:4px solid var(--white);background:radial-gradient(circle at 40% 40%,#7ea36a,#3f6a4c 70%,#2a3f33)}
.mission__title{font-family:"Montserrat",Arial,sans-serif;font-weight:800;color:var(--orange);font-size:18px;line-height:1.2}
.mission__pledge{display:flex;align-items:center;gap:12px;margin:16px 0 12px;text-align:left}
.mission__pct{font-family:"Montserrat",Arial,sans-serif;font-weight:800;font-size:50px;background:var(--white);color:var(--charcoal);padding:0 8px;line-height:1.1}
.mission__pledge p{font-size:11.5px;line-height:1.45}
.mission__cta{font-weight:700;font-size:13px;text-align:left;line-height:1.4;margin-bottom:12px}
.charities{list-style:none;text-align:left}
.charities li{display:grid;grid-template-columns:26px 1fr;gap:8px;margin-bottom:12px}
.charities svg{margin-top:2px}
.charities strong{display:block;font-family:"Montserrat",Arial,sans-serif;color:var(--orange);font-size:12.5px}
.charities span{font-size:11px;line-height:1.4}
.contact{position:absolute;left:30px;right:30px;text-align:center}
.quote-pill{display:flex;align-items:center;justify-content:center;gap:10px;background:var(--orange);color:var(--white);border-radius:20px;height:34px;font-family:"Montserrat",Arial,sans-serif;font-weight:700;font-size:14px}
.quote-pill .phone{display:flex;align-items:center;gap:5px;font-size:15px}
.contact__addr{font-size:11px;margin-top:8px;color:var(--white)}
.contact__web{font-size:12px;font-weight:700;color:var(--white)}

/* cover */
.brand{position:absolute;top:66px;left:20px;right:20px;display:flex;align-items:center;justify-content:center;gap:10px}
.brand__mark{flex:0 0 14px;width:14px;height:14px;border-radius:50%;background:var(--charcoal)}
.brand__name{font-family:"Montserrat",Arial,sans-serif;font-weight:700;font-size:20px;color:var(--charcoal);white-space:nowrap}
.photo--building{top:160px;height:360px;background:linear-gradient(180deg,#b9d4ea 0%,#dfe7ec 35%,#c59068 36%,#8c5b3c 70%,#5b5652 100%)}
.values{position:absolute;top:610px;left:0;right:0;text-align:center;font-family:"Montserrat",Arial,sans-serif;font-weight:800;font-size:26px;line-height:1.25}
.values .navy{color:var(--navy)}
.values .orange{color:var(--orange)}

/* inside */
.service-photo{height:290px}
.service-photo--roofing{background:linear-gradient(160deg,#cfe3f3,#8ea4b7 55%,#44505c)}
.service-photo--construction{background:linear-gradient(180deg,#a9cbe6 0%,#e4e6e4 45%,#9a9a95 75%,#4c4e50)}
.service-photo--restoration{background:linear-gradient(160deg,#3c3c44,#d0541c 45%,#6d6a68 70%,#2a2a2c)}
.service-badge{position:absolute;top:262px;left:50%;transform:translateX(-50%);width:100px;height:100px;border-radius:50%;border:4px solid var(--white);background:radial-gradient(circle at 50% 40%,#b8c7d2,#6a6e70 70%);z-index:2}
.service{position:absolute;left:34px;right:30px;top:340px}
.service--mid{top:375px}
.service__head{text-align:center;margin-bottom:12px}
.service__head h2{font-family:"Montserrat",Arial,sans-serif;font-weight:600;color:var(--orange);font-size:17px;letter-spacing:1px;margin-top:4px}
.bullets{list-style:none;margin-bottom:14px}
.bullets li{font-size:12.5px;line-height:1.55;padding-left:14px;position:relative}
.bullets li::before{content:"";position:absolute;left:0;top:7px;width:6px;height:6px;border-radius:50%;background:var(--orange)}
.service p{font-size:11.5px;line-height:1.55;color:var(--muted);margin-bottom:12px}
.specs{list-style:none}
.specs li{font-size:11px;line-height:1.55;color:var(--muted);padding-left:12px;position:relative}
.specs li::before{content:"•";position:absolute;left:0;color:var(--white)}
</style>
</head>
<body>

<!-- Outside spread -->
<section class="spread spread--outside" aria-label="Brochure outside">
  <article class="panel panel--light">
    <div class="photo photo--founder" role="img" aria-label="Portrait of the company founder"></div>
    <svg class="curve" style="top:240px" viewBox="0 0 367 70" height="70" preserveAspectRatio="none"><path d="M0 40 Q180 -10 367 30 L367 70 L0 70Z" fill="#f6f6f6"/><path d="M0 40 Q180 -10 367 30" fill="none" stroke="#f08a1c" stroke-width="3"/></svg>
    <div class="founder">
      <h2 class="founder__title">Founder &amp; Principal</h2>
      <div class="founder__name">Avery Brantley, Owner</div>
      <p>Brantley Commercial is a woman-owned roofing and construction firm built on decades of hands-on experience in the commercial and industrial building trades.</p>
      <p>We treat every roof as a long-term investment, giving owners honest guidance, clear pricing and a crew that stands behind its work long after the job is done.</p>
      <p>We are committed to quality workmanship, safe job sites and lasting relationships with the building owners and property managers we serve.</p>
    </div>
    <div class="skyline" role="img" aria-label="City skyline silhouette"></div>
  </article>

  <article class="panel panel--dark">
    <div class="mission">
      <div class="mission__photo" role="img" aria-label="Community outreach photo"></div>
      <h2 class="mission__title">FAITH BASED,<br>MISSION MINDED</h2>
      <div class="mission__pledge">
        <span class="mission__pct">10%</span>
        <p>of all Brantley Commercial profits support our mission to restore hope in the lives of those we serve.</p>
      </div>
      <p class="mission__cta">Sign with Brantley Commercial and select one of our sponsored charities:</p>
      <ul class="charities">
        <li><svg width="22" height="22" viewBox="0 0 22 22"><circle cx="11" cy="11" r="8" fill="none" stroke="#f08a1c" stroke-width="2"/><circle cx="11" cy="11" r="3" fill="#f08a1c"/></svg><div><strong>CLEAR SPRINGS WATER FUND</strong><span>Clean water, sanitation and hygiene for families.</span></div></li>
        <li><svg width="22" height="22" viewBox="0 0 22 22"><circle cx="11" cy="11" r="8" fill="none" stroke="#f08a1c" stroke-width="2"/><circle cx="11" cy="11" r="3" fill="#f08a1c"/></svg><div><strong>HOPE HARBOR COMMUNITY CENTER</strong><span>Local meals, shelter and care for our neighbors.</span></div></li>
        <li><svg width="22" height="22" viewBox="0 0 22 22"><circle cx="11" cy="11" r="8" fill="none" stroke="#f08a1c" stroke-width="2"/><circle cx="11" cy="11" r="3" fill="#f08a1c"/></svg><div><strong>SAFE PASSAGE ALLIANCE</strong><span>Prevention, restoration and justice for survivors.</span></div></li>
      </ul>
    </div>
    <div class="contact" style="top:690px">
      <div class="quote-pill">FREE QUOTE <span class="phone"><svg width="14" height="14" viewBox="0 0 24 24"><path d="M6.6 10.8a15 15 0 0 0 6.6 6.6l2.2-2.2c.3-.3.7-.4 1-.2 1.1.4 2.3.6 3.6.6.6 0 1 .4 1 1V20c0 .6-.4 1-1 1A17 17 0 0 1 3 4c0-.6.4-1 1-1h3.5c.6 0 1 .4 1 1 0 1.3.2 2.5.6 3.6.1.3 0 .7-.2 1z" fill="#fff"/></svg>312-555-0148</span></div>
      <p class="contact__addr">4410 Harlow Avenue, Suite B Aurora, IL 60504</p>
      <p class="contact__web">www.brantleyroof.com</p>
    </div>
  </article>

  <article class="panel panel--light">
    <div class="brand">
      <span class="brand__mark"></span>
      <span class="brand__name">Brantley Commercial Roofing</span>
    </div>
    <div class="photo photo--building" role="img" aria-label="Modern commercial building exterior"></div>
    <svg class="curve" style="top:470px" viewBox="0 0 367 80" height="80" preserveAspectRatio="none"><path d="M0 30 Q200 80 367 10 L367 80 L0 80Z" fill="#f6f6f6"/><path d="M0 30 Q200 80 367 10" fill="none" stroke="#f08a1c" stroke-width="6"/><path d="M0 42 Q200 90 367 22" fill="none" stroke="#2e2e2f" stroke-width="2"/></svg>
    <div class="values">
      <div class="navy">KNOWLEDGEABLE</div>
      <div class="orange">TRUSTWORTHY</div>
      <div class="navy">COMMITTED</div>
    </div>
    <div class="skyline" role="img" aria-label="City skyline silhouette"></div>
  </article>
</section>

<!-- Inside spread -->
<section class="spread spread--inside" aria-label="Brochure inside">
  <article class="panel panel--dark">
    <div class="photo service-photo service-photo--roofing" role="img" aria-label="Roofers working on a commercial roof"></div>
    <svg class="curve" style="top:240px" viewBox="0 0 367 70" height="70" preserveAspectRatio="none"><path d="M0 20 Q200 70 367 40 L367 70 L0 70Z" fill="#2e2e2f"/><path d="M0 20 Q200 70 367 40" fill="none" stroke="#f08a1c" stroke-width="5"/></svg>
    <div class="service">
      <div class="service__head">
        <svg width="40" height="26" viewBox="0 0 40 26"><path d="M3 16 L20 4 L37 16" fill="none" stroke="#fff" stroke-width="3" stroke-linejoin="round"/><path d="M9 14 V22 H31 V14" fill="none" stroke="#fff" stroke-width="2"/></svg>
        <h2>ROOFING</h2>
      </div>
      <ul class="bullets">
        <li>New Construction</li><li>Tear off and Replacement</li><li>Vented Full Overlay</li><li>Preventative Maintenance</li><li>Inspections</li>
      </ul>
      <p>Our free roof evaluation will offer you insight to determine whether you are in need of a routine maintenance plan or if the roof is due for repairs, vented overlay or a full replacement.</p>
      <ul class="specs">
        <li>Flat Roof: EPDM, Modified Bitumen, TPO</li><li>Metal Roof: Standing Seam</li><li>Shingles: Standard &amp; Steep Slope Structures</li><li>Glass Atriums + Skylights</li><li>Eco Roofing + Green Roofing</li>
      </ul>
    </div>
    <div class="skyline" role="img" aria-label="City skyline silhouette"></div>
  </article>

  <article class="panel panel--dark">
    <div class="photo service-photo service-photo--construction" role="img" aria-label="Completed two-storey commercial building"></div>
    <svg class="curve" style="top:240px" viewBox="0 0 367 70" height="70" preserveAspectRatio="none"><path d="M0 40 Q180 10 367 40 L367 70 L0 70Z" fill="#2e2e2f"/><path d="M0 40 Q180 10 367 40" fill="none" stroke="#f08a1c" stroke-width="5"/></svg>
    <div class="service-badge" role="img" aria-label="Building entrance detail"></div>
    <div class="service service--mid">
      <div class="service__head">
        <svg width="34" height="28" viewBox="0 0 34 28"><path d="M3 14 L17 3 L31 14" fill="none" stroke="#fff" stroke-width="3" stroke-linejoin="round"/><rect x="8" y="13" width="18" height="12" fill="none" stroke="#fff" stroke-width="2"/><rect x="14" y="17" width="6" height="8" fill="#fff"/></svg>
        <h2>CONSTRUCTION</h2>
      </div>
      <ul class="bullets">
        <li>New Construction 2,500sf +</li><li>Full Out Renovation</li><li>Carpentry</li><li>HVAC / Plumbing / Electrical</li><li>Fire Alarm Systems &amp; Testing</li><li>City Storm Water</li>
      </ul>
      <p>Have a new property build that needs to comply with local standards and regulations? We offer complete project planning and management so you can simply enjoy your new space, on time and on budget.</p>
      <ul class="specs">
        <li>2,500 – 300,000 sf structures</li><li>State and Local Contracts</li><li>Commercial and Municipal Builds</li><li>Commercial Roof Coats</li>
      </ul>
    </div>
    <div class="skyline" role="img" aria-label="City skyline silhouette"></div>
  </article>

  <article class="panel panel--dark">
    <div class="photo service-photo service-photo--restoration" role="img" aria-label="Fire-damaged industrial building with smoke"></div>
    <svg class="curve" style="top:240px" viewBox="0 0 367 70" height="70" preserveAspectRatio="none"><path d="M0 40 Q180 70 367 15 L367 70 L0 70Z" fill="#2e2e2f"/><path d="M0 40 Q180 70 367 15" fill="none" stroke="#f08a1c" stroke-width="5"/></svg>
    <div class="service">
      <div class="service__head">
        <svg width="30" height="30" viewBox="0 0 30 30"><path d="M15 3 C20 11 24 15 24 20 A9 9 0 0 1 6 20 C6 15 10 11 15 3Z" fill="#fff"/></svg>
        <h2>RESTORATION</h2>
      </div>
      <ul class="bullets">
        <li>Fire Restoration</li><li>Smoke Restoration</li><li>Mold Remediation</li><li>Flood Restoration</li><li>Storm Restoration</li>
      </ul>
      <p>Has your property suffered from a fire or natural disaster? Allow us to walk you through the restoration process. Our team works directly with your insurance provider to restore your property and get you back to business quickly.</p>
    </div>
    <div class="contact" style="top:700px">
      <div class="quote-pill">FREE QUOTE <span class="phone"><svg width="14" height="14" viewBox="0 0 24 24"><path d="M6.6 10.8a15 15 0 0 0 6.6 6.6l2.2-2.2c.3-.3.7-.4 1-.2 1.1.4 2.3.6 3.6.6.6 0 1 .4 1 1V20c0 .6-.4 1-1 1A17 17 0 0 1 3 4c0-.6.4-1 1-1h3.5c.6 0 1 .4 1 1 0 1.3.2 2.5.6 3.6.1.3 0 .7-.2 1z" fill="#fff"/></svg>312-555-0148</span></div>
      <p class="contact__addr">4410 Harlow Avenue, Suite B Aurora, IL 60504</p>
      <p class="contact__web">www.brantleyroof.com</p>
    </div>
    <div class="skyline" role="img" aria-label="City skyline silhouette"></div>
  </article>
</section>

</body>
</html>
```